Harrowgate Minerals Web Design

Require a Web page design for an international mining and private investment company currently based in Dubai, UAE. I would like to view designs that incorporate our current corporate logo design aimed at communicating global business development/expansion across a diversity of commodities within the mining and investment sectors.

We are a global organisation with global experience and strategy with specific business development focus in Africa, Central and South America.

Target Market(s)

Mining industry, finance, fund raising, brokering, private equity and public stock exchanges.

Industry/Entity Type

Mining

Number of Pages Required

5+ page

Font styles to use
Sans Serif

Colors

Designer to choose colors to be used in the design.

Requirements
Must have
• Corporate logo, description of who we are, what we do, corporate mission, vision & strategy.
Nice to have
• Inclusion of images, photos, interactive maps/graphics and video.

```html
<!DOCTYPE html>
<html lang="en">
<head>
<meta charset="utf-8">
<title>Harrowgate Minerals</title>
<link href="https://fonts.googleapis.com/css2?family=Lato:wght@400;700;900&family=Open+Sans:wght@400;600&display=swap" rel="stylesheet">
<style>
:root{
  --gold:#c8a55c;
  --gold-dark:#b08d43;
  --gold-light:#dcbf7d;
  --ink:#1b1b1b;
  --text:#555;
  --white:#fff;
  --grey-panel:#d9d9d9;
  --footer:#1c1c1c;
}
*{box-sizing:border-box;margin:0;padding:0}
html,body{width:1200px;height:3158px;overflow:hidden}
body{position:relative;background:var(--white);font-family:'Open Sans',sans-serif;color:var(--text)}
.abs{position:absolute}

/* hero */
.hero{left:0;top:0;width:1200px;height:712px;overflow:hidden;
  background:linear-gradient(180deg,#242a4a 0%,#3a3f50 30%,#5b5a55 60%,#6d6555 100%)}
.hero-photo{left:0;top:0;width:1200px;height:712px;
  background:radial-gradient(ellipse at 50% 60%,rgba(140,120,95,.55),rgba(30,35,60,0) 70%)}
.hero-shape{left:0;top:0}
.brand{left:98px;top:28px;display:flex;align-items:center;gap:10px;white-space:nowrap}
.brand-mark{width:40px;height:40px;border:3px solid var(--gold)}
.brand-name{font-family:'Lato',sans-serif;font-weight:700;font-size:17px;color:var(--gold-light);letter-spacing:.5px;text-transform:uppercase}
.nav{left:410px;top:40px;display:flex;gap:22px;font-family:'Lato',sans-serif;font-weight:700;font-size:13px;color:var(--white);text-transform:uppercase;white-space:nowrap}
.nav .active{color:var(--gold-light)}
.hero-title{left:0;top:265px;width:1200px;text-align:center;font-family:'Lato',sans-serif;font-weight:900;font-size:46px;line-height:50px;color:var(--white);letter-spacing:1px}
.btn{display:inline-block;background:var(--gold);color:var(--white);font-family:'Lato',sans-serif;font-weight:700;text-transform:uppercase}
.hero-btn{left:516px;top:385px;width:172px;height:42px;line-height:42px;text-align:center;font-size:16px;text-transform:none;font-weight:400;
  background:linear-gradient(180deg,var(--gold-light),var(--gold-dark))}
.dots{left:552px;top:628px;display:flex;align-items:center;gap:8px}
.dot{width:8px;height:8px;border-radius:50%;background:rgba(255,255,255,.6)}
.dot.on{background:var(--white)}
.arrow{width:18px;height:18px;border-radius:50%;background:var(--white)}

/* what we do */
.what-box{left:114px;top:819px;width:488px;height:335px;border:2px solid var(--gold)}
.section-heading{font-family:'Lato',sans-serif;font-weight:700;text-transform:uppercase}
.what-heading{left:170px;top:860px;font-size:27px;color:var(--gold)}
.body-copy{font-size:14.5px;line-height:25px;color:var(--text)}
.what-p1{left:172px;top:908px;width:390px}
.what-p2{left:172px;top:973px;width:400px}
.small-btn{height:40px;line-height:40px;text-align:center;font-size:14px}
.what-btn{left:171px;top:1067px;width:144px}
.what-photo{left:602px;top:773px;width:491px;height:421px;box-shadow:0 8px 24px rgba(0,0,0,.3);
  background:radial-gradient(circle at 75% 25%,#f3e2a8 0%,#d9a24e 35%,#8d5a2a 75%,#4a2d17 100%)}

/* projects */
.projects{left:0;top:1326px;width:1200px;height:526px;
  background:linear-gradient(135deg,var(--gold-dark) 0%,var(--gold) 50%,#bd9a50 100%)}
.projects-title{left:0;top:1378px;width:1200px;text-align:center;font-size:27px;color:var(--white);font-weight:400}
.project-card{top:1444px;width:324px;height:286px}
.project-label{top:1673px;height:38px;line-height:38px;background:rgba(255,255,255,.88);text-align:center;font-family:'Lato',sans-serif;font-size:18px;color:var(--ink);text-transform:uppercase}
.projects-edge{left:0;top:1740px}

/* mission */
.info-card{top:1941px;width:480px;height:299px;text-align:center;color:var(--white)}
.card-mission{left:107px;background:linear-gradient(135deg,#4a4844,#5e5a53 60%,#46443f)}
.card-vision{left:617px;background:linear-gradient(135deg,#1d1d1d,#2e2e2c 60%,#1a1a1a)}
.info-icon{position:absolute;left:215px;top:32px}
.info-title{position:absolute;left:0;top:96px;width:100%;font-size:22px;color:var(--white)}
.info-text{position:absolute;left:60px;top:138px;width:360px;font-size:13.5px;line-height:22px;color:#ddd}
.info-btn{position:absolute;left:167px;top:210px;width:146px}

/* who we are */
.who{left:0;top:2326px;width:1200px;height:448px;background:var(--grey-panel)}
.who-photo{left:0;top:2326px;width:720px;height:448px;
  background:linear-gradient(90deg,#5a4136 0%,#8f7a6c 30%,#b8b2ab 60%,rgba(217,217,217,0) 100%)}
.who-heading{left:688px;top:2420px;font-size:27px;color:var(--ink);font-weight:400}
.who-p1{left:688px;top:2466px;width:400px;color:#444}
.who-p2{left:688px;top:2531px;width:400px;color:#444}
.who-btn{left:688px;top:2625px;width:144px}

/* footer */
.footer{left:0;top:2774px;width:1200px;height:384px;background:var(--footer)}
.footer-col{top:2842px;color:#ccc}
.footer-heading{font-family:'Lato',sans-serif;font-weight:400;font-size:18px;color:var(--white);text-transform:uppercase;margin-bottom:14px}
.footer-list{list-style:none;font-size:14.5px;line-height:31px}
.footer-divider{top:2836px;width:1px;height:150px;background:#444}
.contact-row{display:flex;gap:16px;font-size:14.5px;line-height:24px;margin-bottom:6px}
.contact-icon{width:16px;flex:none;padding-top:4px}
.social{display:flex;gap:30px;margin-top:14px}
.social-dot{width:18px;height:18px;border-radius:50%;background:var(--gold)}
.footer-rule{left:127px;top:3088px;width:984px;height:1px;background:#3a3a3a}
.copyright{left:0;top:3111px;width:1200px;text-align:center;font-size:12.5px;color:#888}
</style>
</head>
<body>

<section class="abs hero">
  <div class="abs hero-photo" role="img" aria-label="Aerial view of an open-pit mine with terraced walls"></div>
  <svg class="abs hero-shape" width="1200" height="712" viewBox="0 0 1200 712">
    <polygon points="0,530 180,560 330,552 560,582 760,575 920,520 1060,470 1200,410 1200,712 0,712" fill="#c9a55c"/>
    <polygon points="0,600 330,552 310,712 0,712" fill="#b8954d" opacity=".7"/>
    <polygon points="560,582 760,575 820,712 520,712" fill="#d4b26a" opacity=".7"/>
    <polygon points="1060,470 1200,410 1200,560" fill="#a8853f" opacity=".6"/>
  </svg>
  <div class="abs brand"><span class="brand-mark"></span><span class="brand-name">Harrowgate Minerals</span></div>
  <nav class="abs nav">
    <span class="active">Home</span><span>Who we are</span><span>What we do</span><span>Corporate mission</span><span>Vision &amp; strategy</span><span>Contact us</span>
  </nav>
  <h1 class="abs hero-title">INTERNATIONAL MINING<br>AND PRIVATE INVESTMENT</h1>
  <a class="abs btn hero-btn">Learn More ›</a>
  <div class="abs dots">
    <span class="arrow"></span><span class="dot on"></span><span class="dot"></span><span class="dot"></span><span class="dot"></span><span class="arrow"></span>
  </div>
</section>

<div class="abs what-box"></div>
<h2 class="abs section-heading what-heading">What we do</h2>
<p class="abs body-copy what-p1">Praesent elementum elit at tellus nec ultricies sit amet porttitor mattis enim In massa libero</p>
<p class="abs body-copy what-p2">interdum nec interdum vel blandit sed nulla In ullamcorper est eget tempor cursus neque mi consecte tuer mi a ultricies massa est sed nisl Class</p>
<a class="abs btn small-btn what-btn">Read more</a>
<div class="abs what-photo" role="img" aria-label="Hand placing coins on growing stacks with seedlings"></div>

<section class="abs projects"></section>
<h2 class="abs section-heading projects-title">Our projects</h2>
<div class="abs project-card" style="left:95px;background:linear-gradient(135deg,#3a3633,#6b645c 60%,#2d2a27)" role="img" aria-label="Business meeting with documents and laptop"></div>
<div class="abs project-card" style="left:438px;background:linear-gradient(180deg,#5b86b8 0%,#9fb3c0 30%,#8a6a45 55%,#6b4a2c 100%)" role="img" aria-label="Excavated mining site under a blue sky"></div>
<div class="abs project-card" style="left:781px;background:linear-gradient(135deg,#3b3631,#6e6053 50%,#4a4038)" role="img" aria-label="Haul road winding through an open-pit mine"></div>
<div class="abs project-label" style="left:106px;width:302px">Project title here</div>
<div class="abs project-label" style="left:449px;width:302px">Project title here</div>
<div class="abs project-label" style="left:792px;width:302px">Project title here</div>
<svg class="abs projects-edge" width="1200" height="113" viewBox="0 0 1200 113">
  <polygon points="0,113 0,95 140,102 280,90 400,60 540,52 610,28 690,66 820,78 960,90 1080,85 1200,100 1200,113" fill="#fff"/>
</svg>

<article class="abs info-card card-mission" role="img" aria-label="Team working over charts at a desk, darkened">
  <svg class="info-icon" width="50" height="50" viewBox="0 0 50 50" fill="none" stroke="#fff" stroke-width="2">
    <path d="M32 8 C40 6 44 10 42 18 L26 34 L16 24 Z"/><circle cx="33" cy="17" r="3"/><path d="M16 24 L8 26 L14 18 L22 18"/><path d="M26 34 L24 42 L32 36 L32 28"/><path d="M14 36 L8 42"/>
  </svg>
  <h3 class="section-heading info-title">Corporate mission</h3>
  <p class="info-text">Praesent elementum elit at tellus nec ultricies sit amet porttitor mattis enim In massa libero interdum nec interdum vel blandit</p>
  <a class="btn small-btn info-btn">Read more</a>
</article>
<article class="abs info-card card-vision" role="img" aria-label="Heavy mining truck at work, darkened">
  <svg class="info-icon" width="50" height="50" viewBox="0 0 50 50" fill="none" stroke="#fff" stroke-width="2">
    <path d="M25 12 C17 12 13 18 13 23 C13 28 18 31 19 35 L31 35 C32 31 37 28 37 23 C37 18 33 12 25 12 Z"/><path d="M20 39 H30 M21 43 H29"/><path d="M25 2 V7 M8 8 L12 12 M42 8 L38 12 M3 23 H8 M42 23 H47"/>
  </svg>
  <h3 class="section-heading info-title">Vision &amp; strategy</h3>
  <p class="info-text">Praesent elementum elit at tellus nec ultricies sit amet porttitor mattis enim In massa libero interdum nec interdum vel blandit</p>
  <a class="btn small-btn info-btn">Read more</a>
</article>

<section class="abs who"></section>
<div class="abs who-photo" role="img" aria-label="Colleagues talking in a bright open-plan office"></div>
<h2 class="abs section-heading who-heading">Who we are</h2>
<p class="abs body-copy who-p1">Praesent elementum elit at tellus nec ultricies sit amet porttitor mattis enim In massa libero</p>
<p class="abs body-copy who-p2">interdum nec interdum vel blandit sed nulla In ullamcorper est eget tempor cursus neque mi consecte tuer mi a ultricies massa est sed nisl Class</p>
<a class="abs btn small-btn who-btn">Read more</a>

<footer class="abs footer"></footer>
<div class="abs footer-col" style="left:116px">
  <h4 class="footer-heading">Company</h4>
  <ul class="footer-list"><li>Home</li><li>Who we are</li><li>What we do</li><li>Corporate mission</li></ul>
</div>
<div class="abs footer-divider" style="left:272px"></div>
<div class="abs footer-col" style="left:320px">
  <h4 class="footer-heading">Resources</h4>
  <ul class="footer-list"><li>Vision &amp; strategy</li><li>News</li><li>Sitemap</li><li>Contact us</li></ul>
</div>
<div class="abs footer-divider" style="left:487px"></div>
<div class="abs footer-col" style="left:539px">
  <h4 class="footer-heading">Contact us</h4>
  <div class="contact-row"><svg class="contact-icon" width="16" height="20" viewBox="0 0 16 20"><path d="M8 0C3.6 0 0 3.4 0 7.6 0 13 8 20 8 20s8-7 8-12.4C16 3.4 12.4 0 8 0zm0 10.5A3 3 0 1 1 8 4.5a3 3 0 0 1 0 6z" fill="#fff"/></svg><span>48 Ridgeline Avenue #4B<br>Denver 80202 CO</span></div>
  <div class="contact-row"><svg class="contact-icon" width="16" height="16" viewBox="0 0 16 16"><path d="M3.5 0 6 3.8 4.4 5.6C5.3 7.6 8.4 10.7 10.4 11.6L12.2 10 16 12.5 14.5 16C7 15.5.5 9 0 1.5Z" fill="#fff"/></svg><span>555.014.2387</span></div>
  <div class="contact-row"><svg class="contact-icon" width="16" height="12" viewBox="0 0 16 12"><rect width="16" height="12" fill="#fff"/><path d="M0 0 8 7 16 0" fill="none" stroke="#1c1c1c" stroke-width="1.5"/></svg><span>info@harrowgateminerals.com</span></div>
</div>
<div class="abs footer-divider" style="left:832px"></div>
<div class="abs footer-col" style="left:901px">
  <h4 class="footer-heading">Follow us</h4>
  <div class="social">
    <span class="social-dot" role="img" aria-label="Social profile link"></span>
    <span class="social-dot" role="img" aria-label="Social profile link"></span>
    <span class="social-dot" role="img" aria-label="Social profile link"></span>
    <span class="social-dot" role="img" aria-label="Social profile link"></span>
  </div>
</div>
<div class="abs footer-rule"></div>
<p class="abs copyright">© 2018 Harrowgate Minerals. All right reserved</p>

</body>
</html>
```